Tourism Marketing needing sleek, clear design for business card & proposal documents.

***Company background***
"Quiet Harbour" is a company specializing in tourism marketing and project management. We do international wholesale, event management as well as ongoing representation of tourism and hospitality companies.

***Target market***
We cater to tourism companies and hotel professionals.

***Task***
We would like to get a single sided business card designed (but will still consider two sided, we are open to any ideas you may have). The layout for this card should be modern and elegant. Currently we do not have a logo, but we would like our business name in a really simple typography for the business card (similar to Moonrise Palace's logo - www.moonrisepalace-example.com.au).We are after a design that is clear, strong enough to be recognised as Quiet Harbour that does not require any fancy design. Another option is a simple play on QH (Quiet Harbour) or simply have Quiet Harbour featured elsewhere on card more as a brand/logo.

Feel free to submit different fonts if you feel you have any other fonts/designs that may be suitable for this card other than sans serifs. Should this project be successful, we will be considering several other projects for business proposal templates and eventually a website design.

The information that needs to go on the card are as follows:

Marta Holloway
Director
Quiet Harbour
Tourism Marketing & Representation
87 Wendover Parade
Larchmont, Victoria, 3999 Australia
T +61 498203617 E marta@quietharbour-example.com.au

***Look and feel***
We'd like the business card design to express the following:
Modern, sleek, elegant, simple, discreet, quality, subtle, professional, creative, innovation

In terms of typography, we like something really simple and blocky (similar font to Moonrise Palace's logo - www.moonrisepalace-example.com.au)

***Colour scheme***
Shades of grey and dark teal

***Note***
Although our main target market are professionals, we would like the business card design to be versatile enough to be used outside of the tourism industry and need to appeal to different markets.

I do not have existing logo. Was hoping for a design that may be clear, strong enough not to require one. Other option is a simple play on QH (Quiet Harbour) or simply have Quiet Harbour featured elsewhere on card more as a brand/logo.

Marta Holloway
Director
Quiet Harbour Pty Ltd 
87 Wendover Parade
T +61 498203617  E  marta@quietharbour-example.com.au

Thank you for designs so far. Many have used a mauve colour which matches our company profile. This is not necessary, as that is just a draft and will be completely redesigned, so dont  feel you need to incorporate the mauve.

My colour preferences are for a white or grey background, and I like fonts in dark teals, grey or other sophisticated but modern colours. feel free to submit different fonts if you you have other fonts you thing would be suitable for this card, along with sans serifs. Should this project be successful, we will be considering several others for business proposal templates and eventually website. 

Target Market(s)

International Hospitality Senior Executives, Directors of International Tourism Companies, Directors of Tourism Bodies Internationally, local Tourism

Industry/Entity Type

Hospitality

Requirements
Should not have
• must not have bright garish colour, swirly patterns or anything that dates too much.

```html
<!DOCTYPE html>
<html lang="en">
<head>
<meta charset="utf-8">
<title>Quiet Harbour – Business Card</title>
<link rel="stylesheet" href="https://fonts.googleapis.com/css2?family=Mulish:wght@400;700&display=swap">
<style>
  :root {
    --page: #ffffff;
    --mauve: #8e6d8b;
    --brand-grey: #a9a9ab;
    --text-grey: #7a7a7c;
    --card-white: #ffffff;
    --card-shadow: rgba(0, 0, 0, 0.22);
  }
  * { margin: 0; padding: 0; box-sizing: border-box; }
  html, body {
    width: 900px; height: 1200px; overflow: hidden;
    background: var(--page);
    font-family: "Mulish", "Verdana", sans-serif;
  }
  .sheet { position: relative; width: 900px; height: 1200px; }

  .card {
    position: absolute; left: 75px; width: 756px; height: 438px;
    box-shadow: 4px 6px 10px var(--card-shadow);
  }
  .card--front { top: 72px; background: var(--card-white); border: 1px solid #e4e4e4; }
  .card--back { top: 680px; background: var(--mauve); color: #fff; }

  /* Front */
  .front-brand {
    position: absolute; right: 48px; top: 42px;
    font-size: 38px; font-weight: 400; letter-spacing: 0.5px;
    color: var(--brand-grey); text-transform: uppercase; white-space: nowrap;
  }
  .name-marker {
    position: absolute; left: 0; top: 213px; width: 24px; height: 55px;
    background: var(--mauve);
  }
  .contact { position: absolute; left: 36px; top: 213px; color: var(--text-grey); }
  .contact__name { font-size: 27px; font-weight: 700; color: var(--mauve); line-height: 32px; letter-spacing: 0.3px; }
  .contact__role { font-size: 17px; line-height: 22px; }
  .contact__company { margin-top: 26px; font-size: 17px; font-weight: 700; color: var(--mauve); line-height: 23px; }
  .contact__line { font-size: 16px; line-height: 23px; white-space: nowrap; }
  .contact__reach { display: flex; align-items: center; margin-top: 4px; font-size: 16px; line-height: 23px; white-space: nowrap; }
  .reach-key {
    display: inline-flex; align-items: center; justify-content: center;
    width: 19px; height: 19px; background: var(--text-grey); color: #fff;
    font-size: 12px; font-weight: 700; margin-right: 6px;
  }
  .reach-item { display: inline-flex; align-items: center; margin-right: 14px; }

  /* Back */
  .back-brand {
    position: absolute; left: 0; right: 0; top: 148px; text-align: center;
    font-size: 48px; font-weight: 400; letter-spacing: 0.5px; text-transform: uppercase;
    line-height: 60px; white-space: nowrap;
  }
  .back-web {
    position: absolute; left: 0; right: 0; top: 234px; text-align: center;
    font-size: 14px; letter-spacing: 5px; white-space: nowrap;
  }
  .services {
    position: absolute; left: 38px; right: 44px; bottom: 44px;
    display: flex; justify-content: space-between; list-style: none;
    font-size: 16px; white-space: nowrap;
  }
  .services li { display: flex; }
  .services li + li::before { content: "|"; margin-right: 24px; opacity: 0.85; }
</style>
</head>
<body>
<main class="sheet">
  <section class="card card--front" aria-label="Business card front">
    <div class="front-brand">Quiet Harbour</div>
    <div class="name-marker"></div>
    <div class="contact">
      <p class="contact__name">Marta Holloway</p>
      <p class="contact__role">Director</p>
      <p class="contact__company">Quiet Harbour Pty Ltd</p>
      <p class="contact__line">Tourism Marketing &amp; Representation</p>
      <p class="contact__line">87 Wendover Parade, Larchmont, Victoria, 3999 Australia</p>
      <p class="contact__reach">
        <span class="reach-item"><span class="reach-key">T</span>+61 498203617</span>
        <span class="reach-item"><span class="reach-key">E</span>marta@quietharbour-example.com.au</span>
      </p>
    </div>
  </section>

  <section class="card card--back" aria-label="Business card back">
    <div class="back-brand">Quiet Harbour</div>
    <p class="back-web">www.quietharbour-example.com.au</p>
    <ul class="services">
      <li>Sales</li>
      <li>Marketing</li>
      <li>Events</li>
      <li>Public Relations</li>
      <li>Reporting</li>
    </ul>
  </section>
</main>
</body>
</html>
```